We are seeking two label designs for our premium pecan snack brand, TORVELLO. TORVELLO is known for its innovative pecan snacks, specifically a healthy and exotic blend of pecans, expertly salted, and infused with unique chili flavors. Our snacks are packaged in stand-up pouch bags, and we are looking for label designs product sizes - 5 oz. ( Size: 14 x 20 cm / 5.5 x 7.8 inches / Max Capacity: 16.2 oz)

Background Information:
TORVELLO is a brand committed to offering a delightful snacking experience that combines the natural richness of pecans with the bold and exotic kick of carefully selected chilies. Our snacks cater to health-conscious consumers who appreciate the fusion of premium quality, unique flavors, and nutritional goodness.

Target Market(s)

Event Attendees (Entertainment Industry), Health-Conscious Consumers

Industry/Entity Type

Entertainment (sports events, arenas, stadiums, etc)

Font styles to use
Other font styles liked:
• Brother1816 Printed

Colors

Designer to choose colors to be used in the design.

Requirements
Must have
• Nutrition Fact (attached) , TRANSPARENT PART LIKE A WINDOW TO DISPLAY THE PRODUCT

```html
<!DOCTYPE html>
<html lang="en">
<head>
<meta charset="utf-8">
<title>TORVELLO – Spicy Roasted Pecans 5oz Label</title>
<link href="https://fonts.googleapis.com/css2?family=Mulish:wght@400;600&display=swap" rel="stylesheet">
<style>
  :root {
    --bg-orange: #ff7a4b;
    --pouch-black: #111113;
    --pouch-edge: #1c1c1f;
    --brand-white: #ffffff;
    --chili-orange: #f26a2a;
    --caption-grey: #c9c9c9;
    --window-frame: #9a9a9c;
    --pecan-dark: #5a2a14;
    --pecan-mid: #8a4a26;
    --pecan-light: #b77a4c;
  }
  * { margin: 0; padding: 0; box-sizing: border-box; }
  html, body {
    width: 1200px;
    height: 1000px;
    overflow: hidden;
    background: var(--bg-orange);
    font-family: "Mulish", sans-serif;
  }
  .canvas {
    position: relative;
    width: 1200px;
    height: 1000px;
  }
  .pouch-label {
    position: absolute;
    left: 330px;
    top: 115px;
    width: 540px;
    height: 770px;
    background: var(--pouch-black);
    border-radius: 6px;
    overflow: hidden;
  }
  .zip-line {
    position: absolute;
    left: 0;
    right: 0;
    top: 58px;
    height: 3px;
    background: var(--pouch-edge);
  }
  .brand-name {
    position: absolute;
    top: 190px;
    left: 0;
    right: 0;
    text-align: center;
    color: var(--brand-white);
    font-weight: 600;
    font-size: 68px;
    letter-spacing: 4px;
    line-height: 1;
  }
  .product-name {
    position: absolute;
    top: 312px;
    left: 0;
    right: 0;
    text-align: center;
    color: var(--chili-orange);
    font-size: 15px;
    font-weight: 400;
  }
  .net-weight {
    position: absolute;
    top: 334px;
    left: 0;
    right: 0;
    text-align: center;
    color: var(--caption-grey);
    font-size: 14px;
    font-weight: 400;
  }
  .product-window {
    position: absolute;
    left: 0;
    right: 0;
    top: 485px;
    height: 150px;
    border-top: 4px solid var(--window-frame);
    border-bottom: 2px solid var(--window-frame);
    border-left: 22px solid var(--window-frame);
    border-right: 22px solid var(--window-frame);
    background: radial-gradient(ellipse at 50% 55%, var(--pecan-light) 0%, var(--pecan-mid) 45%, var(--pecan-dark) 100%);
  }
</style>
</head>
<body>
  <main class="canvas">
    <section class="pouch-label">
      <div class="zip-line"></div>
      <h1 class="brand-name">TORVELLO</h1>
      <p class="product-name">Spicy Roasted Pecans</p>
      <p class="net-weight">5oz (142g)</p>
      <div class="product-window" role="img" aria-label="Clear window showing the spicy roasted pecan halves inside the pouch"></div>
    </section>
  </main>
</body>
</html>
```